Stylist/Barber Standup Sign for Hair Regrowth Company

We want to design an attractive and eye-catching sign for hair stylists and barbers to sit on their workstations to attract the attention of their clients regarding hair loss and encourage them to speak to their stylist about it of they are would like to seek treatment.
50% of men and 25% of women suffer from hair loss but most are in denial that it is happening or too embarrassed to talk about it.

Copy for the flyer is as follows:

[Section 1:]
This flyer has been placed here/designed to spark conversation about hair loss

[Section 2:]
The truth is...
73% of people believe their hair is thinning
They are right

[Section 3:]
If you've got questions, your stylist or barber has answers.

Additional Background Information:

Primary target audience is men between the ages of 25-45, secondary target audience is men 46-60

Current Consumer Perception? (in the first person) “I’ve been thinking about my hair. I think it’s getting thinner and I’m scared, worried and don’t know what to do. But I don’t know if there is anything that really works. I’ve tried other things and nothing‘s worked.”

Tonality of materials? Very guy friendly, matter of fact, authoritative, its what you might hear from your best friend. Confident. Encouraging, but with a sense of urgency.

Please use our brand colors, but do not include our logo or brand name.
Colors are as follows:
Green: #4ca26f
Light Grey: #999999
Dark Grey: #262626

I have attached print templates in both PDF and Jpeg, please use those to provide final ready to print documents if you are selected.

Target Market(s)

Industry/Entity Type

Health And Wellness

Font styles to use
Sans Serif

Colors
00a990
ffffff
333333
cbcbcb

Requirements
Must have
• We want to get across the following messaging. Ideally you will submit a design using our copy and if you think you can do better, please feel free to submit another design with your own copy/messaging. If you can do it better we would love to select you :-)
• Our copy?
• This flyer has been placed here/designed to spark conversation about hair loss
• The truth is...
• 73% of people believe their hair is thinning
• They are right
• If you've got questions, your stylist or barber has answers
• Also please use our brand colors:
• Green: #4ca26f
• Light Grey: #999999
• Dark Grey: #262626
Should not have
• dont add any logos, images or ornate design. this needs to be simple, easy to ready and eye catching.
• do not use the color red in any capacity.

```html
<!DOCTYPE html>
<html lang="en">
<head>
<meta charset="utf-8">
<title>Hair Loss &amp; Regrowth – Workstation Sign</title>
<link rel="stylesheet" href="https://fonts.googleapis.com/css2?family=Montserrat:wght@400;500;600;700;800;900&display=swap">
<style>
  :root {
    --teal: #00a990;
    --ink: #333333;
    --dark: #2b2b2b;
    --grey: #cbcbcb;
    --band: #eeeded;
    --white: #ffffff;
  }
  html, body { margin: 0; padding: 0; overflow: hidden; background: var(--white); }
  .sign {
    position: relative;
    width: 880px;
    height: 1200px;
    overflow: hidden;
    background: var(--white);
    font-family: "Montserrat", sans-serif;
    color: var(--ink);
  }
  .abs { position: absolute; line-height: 1; margin: 0; white-space: nowrap; }

  .header-wave { position: absolute; left: 0; top: 0; width: 880px; height: 440px; }

  .title { left: 39px; top: 22px; color: #e9e9e9; font-weight: 800; font-size: 58px; letter-spacing: -0.5px; line-height: 0.98; }
  .title .amp { font-weight: 400; }
  .title .big { color: var(--white); font-size: 66px; }

  .portrait-ring { position: absolute; left: 564px; top: 45px; width: 270px; height: 270px; border-radius: 50%; background: var(--grey); }
  .portrait-art { position: absolute; left: 17px; top: 17px; width: 236px; height: 236px; border-radius: 50%; background: var(--teal); }

  .bubble {
    position: absolute; left: 53px; top: 254px; width: 241px; height: 225px;
    border: 2px solid var(--teal); border-radius: 12px; background: var(--white);
    box-shadow: 3px 4px 0 rgba(0,0,0,0.12);
    display: flex; align-items: center; justify-content: center; text-align: center;
    font-weight: 700; font-size: 23px; line-height: 1.45; color: var(--ink);
  }
  .bubble-tail { position: absolute; left: 292px; top: 310px; width: 46px; height: 46px; }

  .conversation-art {
    position: absolute; left: 330px; top: 300px; width: 330px; height: 231px;
    background: var(--teal); border-radius: 90px 90px 0 0;
  }

  .stat-band { position: absolute; left: 0; top: 531px; width: 880px; height: 319px; background: var(--band); }
  .donut { position: absolute; left: 55px; top: 559px; width: 268px; height: 268px; }

  .truth { left: 372px; top: 572px; color: var(--teal); font-weight: 700; font-size: 47px; }
  .stat-line { left: 385px; color: var(--ink); font-weight: 600; font-size: 29px; }
  .stat-line.one { top: 627px; }
  .stat-line.two { top: 668px; }
  .stat-accent { left: 385px; top: 710px; color: var(--teal); font-weight: 800; font-size: 29px; }
  .verdict { left: 385px; top: 745px; color: var(--teal); font-weight: 700; font-size: 54px; }

  .lead { left: 51px; top: 893px; color: var(--teal); font-weight: 500; font-size: 46px; }
  .questions { left: 46px; top: 943px; color: var(--ink); font-weight: 900; font-size: 80px; letter-spacing: -2px; }
  .client-art { position: absolute; left: 606px; top: 877px; width: 118px; height: 130px; background: var(--teal); border-radius: 55px 55px 8px 8px; }
  .stylist-art { position: absolute; left: 240px; top: 1022px; width: 80px; height: 118px; background: var(--teal); border-radius: 40px 40px 6px 6px; }
  .reply { left: 334px; top: 1023px; color: var(--teal); font-weight: 500; font-size: 37px; }
  .answers { left: 330px; top: 1073px; color: var(--ink); font-weight: 900; font-size: 80px; letter-spacing: -2px; }

  .footer-bar { position: absolute; left: 0; top: 1167px; width: 880px; height: 33px; background: var(--teal); }
</style>
</head>
<body>
<main class="sign">
  <svg class="header-wave" viewBox="0 0 880 440" aria-hidden="true">
    <path d="M0 0 H880 V420 C820 405 760 380 705 330 C610 250 510 300 400 292 C250 282 120 172 0 184 Z" fill="var(--dark)"/>
    <path d="M0 202 C130 180 250 300 400 310 C500 318 560 290 620 292" fill="none" stroke="var(--white)" stroke-width="5"/>
    <path d="M640 370 C700 420 790 430 880 428" fill="none" stroke="var(--white)" stroke-width="5"/>
  </svg>

  <h1 class="abs title">HAIR LOSS <span class="amp">&amp;</span><br><span class="big">REGROWTH</span></h1>

  <div class="portrait-ring">
    <div class="portrait-art" role="img" aria-label="Teal silhouettes of a woman and a man in profile, back to back"></div>
  </div>

  <p class="bubble">Spark<br>Conversation<br>About Hair<br>Loss With Hair<br>Stylists And<br>Barbers</p>
  <svg class="bubble-tail" viewBox="0 0 46 46" aria-hidden="true">
    <path d="M0 4 L44 30 L0 26" fill="var(--white)" stroke="var(--teal)" stroke-width="2"/>
  </svg>

  <div class="conversation-art" role="img" aria-label="Teal silhouettes of a client and a barber talking"></div>

  <section class="stat-band" aria-hidden="false"></section>
  <svg class="donut" viewBox="0 0 268 268" aria-hidden="true">
    <circle cx="134" cy="134" r="120" fill="none" stroke="var(--grey)" stroke-width="28"/>
    <circle cx="134" cy="134" r="120" fill="none" stroke="var(--dark)" stroke-width="28"
            stroke-dasharray="550 754" transform="rotate(-90 134 134) scale(1 -1) translate(0 -268)"/>
    <text x="134" y="160" text-anchor="middle" font-family="Montserrat, sans-serif" font-weight="800" font-size="72" fill="var(--dark)">73%</text>
  </svg>

  <h2 class="abs truth">The Truth is...</h2>
  <p class="abs stat-line one">of People</p>
  <p class="abs stat-line two">Believe their</p>
  <p class="abs stat-accent">HAIR IS THINNING</p>
  <p class="abs verdict">They are Right</p>

  <p class="abs lead">If you've got</p>
  <p class="abs questions">QUESTIONS</p>
  <div class="client-art" role="img" aria-label="Teal silhouette of a woman with long hair gesturing a question"></div>
  <div class="stylist-art" role="img" aria-label="Teal silhouette of a man in profile"></div>
  <p class="abs reply">your stylist or barber has</p>
  <p class="abs answers">ANSWERS</p>

  <div class="footer-bar"></div>
</main>
</body>
</html>
```